Rehab/fitness Business card design

I need a design that promotes "A ready made base for runners". services include assessment, massage, physiotherapy, pilates, suspension training, kinesiotaping in any combination.
I would like to bring the design into my website, flyers etc

Target Market(s)

athletes from beginner to elite - any age, male and female

Industry/Entity Type

Shop

Contact Information for Business Card

Ready-Made-Base for Runners
17 Parvel Crescent, Hollowmere, Tauranga
021 847 3610
gwen.farrowby@quillmail.test

Logo Text

Requirements
Nice to have
• Blue colour theme

```html
<!DOCTYPE html>
<html lang="en">
<head>
<meta charset="utf-8">
<title>Ready-Made-Base for Runners – Business Card</title>
<link rel="stylesheet" href="https://fonts.googleapis.com/css2?family=Barlow:wght@300;400;700&display=swap">
<style>
  :root {
    --card-blue: #0082ff;
    --deep-blue: #0a14f0;
    --figure-blue: #0a4dff;
    --frame: #0b1a3a;
    --white: #ffffff;
  }
  html, body {
    margin: 0;
    padding: 0;
    overflow: hidden;
    background: #ffffff;
  }
  .card {
    position: relative;
    width: 1200px;
    height: 693px;
    box-sizing: border-box;
    background: var(--card-blue);
    border: 2px solid var(--frame);
    overflow: hidden;
    font-family: "Barlow", "Helvetica Neue", Arial, sans-serif;
    color: var(--white);
  }
  .card > * { position: absolute; margin: 0; line-height: 1; white-space: nowrap; }

  .runner-figure {
    left: 80px;
    top: 246px;
    width: 292px;
    height: 386px;
  }

  .headline {
    left: 68px;
    top: 50px;
    font-size: 92px;
    font-weight: 700;
    color: var(--deep-blue);
    letter-spacing: 0.5px;
  }
  .subhead {
    left: 68px;
    top: 143px;
    font-size: 63px;
    font-weight: 400;
    color: var(--white);
  }
  .subhead .accent { color: var(--deep-blue); }

  .services-title {
    right: 77px;
    top: 214px;
    font-size: 35px;
    font-weight: 400;
  }
  .services-list {
    right: 77px;
    top: 262px;
    list-style: none;
    padding: 0;
    text-align: right;
    font-size: 34px;
    font-weight: 300;
    line-height: 42px;
  }

  .address {
    left: 66px;
    top: 566px;
    font-size: 29px;
    font-weight: 300;
  }
  .contact-line {
    left: 66px;
    top: 604px;
    font-size: 29px;
    font-weight: 300;
  }
  .contact-line .email { position: absolute; left: 304px; }
</style>
</head>
<body>
  <div class="card">
    <svg class="runner-figure" viewBox="0 0 292 386" role="img" aria-label="Silhouette illustration of a running athlete">
      <rect x="0" y="0" width="292" height="386" rx="60" fill="var(--figure-blue)" opacity="0.55"/>
    </svg>

    <h1 class="headline">READY-MADE-BASE</h1>
    <p class="subhead"><span class="accent">FOR</span> RUNNERS</p>

    <h2 class="services-title">OUR SERVICES</h2>
    <ul class="services-list">
      <li>Assessment</li>
      <li>Massage</li>
      <li>Physiotherapy</li>
      <li>Pilates</li>
      <li>Suspension Training</li>
      <li>Kinesiotaping in Any Combination</li>
    </ul>

    <p class="address">17 Parvel Crescent, Hollowmere, Tauranga</p>
    <p class="contact-line"><span class="phone">Tel. 021 847 3610</span><span class="email">gwen.farrowby@quillmail.test</span></p>
  </div>
</body>
</html>
```